Simple and clean

We need a business card design for a new company called Dwelling Owl. It is a search engine to find current properties for sale or rent in New Zealand market.
We have already a colour scheme that we would like people to use.
Light brown: #D4CCB0
Light green: #D6E4D4
Green: #669966
Black/White
It is OK to divert from this colour scheme slightly as long as there is a green component to the business card.
Final design should be clean, simple and should communicate the nature of the business.
Target Market(s)
- First home buyers
- Real estate agents
- People seeking rentals
Industry/Entity Type
Business
Requirements
Must have
- Use those or similar colours.
Light brown: #D4CCB0
Light green: #D6E4D4
Green: #669966
Black/White

```html
<!DOCTYPE html>
<html lang="en">
<head>
<meta charset="utf-8">
<title>Dwelling Owl – Business Card</title>
<link rel="stylesheet" href="https://fonts.googleapis.com/css2?family=Poppins:wght@300;400;600&display=swap">
<style>
  :root {
    --backdrop: #2b2b2b;
    --card-white: #fbfcfa;
    --card-tint: #e4ede2;
    --green: #669966;
    --light-green: #d6e4d4;
    --ink: #1e1e1e;
    --muted: #9a9a9a;
    --white: #ffffff;
  }
  * { margin: 0; padding: 0; box-sizing: border-box; }
  html, body {
    width: 1200px;
    height: 851px;
    overflow: hidden;
    background: var(--backdrop);
    font-family: "Poppins", sans-serif;
  }
  .stage {
    position: relative;
    width: 1200px;
    height: 851px;
  }
  .business-card {
    position: absolute;
    left: 160px;
    top: 175px;
    width: 880px;
    height: 500px;
    border-radius: 26px;
    overflow: hidden;
    background: linear-gradient(100deg, var(--card-white) 0%, var(--card-white) 35%, var(--card-tint) 100%);
  }
  .brand {
    position: absolute;
    left: 80px;
    top: 72px;
    display: flex;
    align-items: center;
    gap: 16px;
  }
  .brand-dot {
    width: 54px;
    height: 54px;
    border-radius: 50%;
    background: var(--green);
  }
  .brand-name {
    font-weight: 600;
    font-size: 40px;
    color: var(--ink);
    letter-spacing: -0.5px;
  }
  .holder {
    position: absolute;
    left: 505px;
    top: 302px;
  }
  .holder-name {
    font-weight: 300;
    font-size: 50px;
    line-height: 1;
    color: var(--ink);
  }
  .holder-role {
    margin-top: 8px;
    font-weight: 300;
    font-size: 20px;
    letter-spacing: 3px;
    color: var(--muted);
  }
  .contact-band {
    position: absolute;
    left: 0;
    bottom: 0;
    width: 100%;
    height: 64px;
    background: var(--green);
    display: flex;
    align-items: center;
    padding-left: 60px;
    color: var(--white);
    font-size: 19px;
    font-weight: 300;
    white-space: nowrap;
  }
  .contact-band .label { font-weight: 600; margin-right: 7px; }
  .contact-band .sep { margin: 0 10px; }
</style>
</head>
<body>
  <main class="stage">
    <section class="business-card">
      <div class="brand">
        <span class="brand-dot"></span>
        <span class="brand-name">Dwelling Owl</span>
      </div>
      <div class="holder">
        <p class="holder-name">Mara Kensington</p>
        <p class="holder-role">director</p>
      </div>
      <footer class="contact-band">
        <span class="label">mobile</span><span>021 - 555 - 014</span>
        <span class="sep">|</span>
        <span class="label">email</span><span>hello@dwellingowl.com</span>
        <span class="sep">|</span>
        <span class="label">web</span><span>www.dwellingowl.co.nz</span>
      </footer>
    </section>
  </main>
</body>
</html>
```